Brightmere Business Card Redesign & Logo Update

We need to update our business cards to something more modern and fresh. Brightmere can provide the current color schemes and old design examples, but welcome creativity in helping us with this redesign. PLEASE NOTE that we no longer utilize the "tree" and/or "leaf" imagery in our branding. If able would apprecaite an update on the quality of our "words only" logo in Ai. / PNG formats too.

Target Market(s)

Investors, landowners, corporate partners, contractors

Industry/Entity Type

Environmental Restoration & Conservation

Contact Information for Business Card

Logo, persons name, title, mailing address, phone and email, website url

Font styles to use
Other font styles liked:
• Merriweather

Requirements
Nice to have
• Logo, persons name, title, mailing address, phone and email, website url, but open to ideams
Should not have
• No all back backgrounds

```html
<!DOCTYPE html>
<html lang="en">
<head>
<meta charset="utf-8">
<title>Brightmere Business Card</title>
<link rel="stylesheet" href="https://fonts.googleapis.com/css2?family=Bebas+Neue&family=Arimo:wght@400&display=swap">
<style>
  :root {
    --stage-green: #1fa000;
    --brand-green: #1e9a0c;
    --brand-orange: #ff6a0c;
    --ink: #111111;
    --card-white: #ffffff;
    --pattern-tint: #dbead2;
  }
  html, body {
    margin: 0;
    padding: 0;
    width: 960px;
    height: 1200px;
    overflow: hidden;
    background: var(--stage-green);
  }
  .stage {
    position: relative;
    width: 960px;
    height: 1200px;
    background: var(--stage-green);
  }
  .card {
    position: absolute;
    left: 60px;
    width: 840px;
    height: 480px;
    border-radius: 48px;
    overflow: hidden;
    background: var(--card-white);
    box-shadow: 0 14px 22px rgba(0, 0, 0, 0.35);
  }
  .card--front { top: 78px; }
  .card--back { top: 642px; }
  .card__pattern {
    position: absolute;
    inset: 0;
    background: radial-gradient(ellipse at center, #ffffff 0%, #f3f8ef 45%, var(--pattern-tint) 100%);
  }
  .wordmark {
    position: absolute;
    left: 0;
    right: 0;
    text-align: center;
    font-family: "Bebas Neue", "Arial Narrow", sans-serif;
    line-height: 1;
    margin: 0;
  }
  .wordmark__name { color: var(--brand-green); }
  .wordmark__tagline { color: var(--ink); }

  .card--front .wordmark__name { top: 218px; font-size: 168px; letter-spacing: 1px; }
  .card--front .wordmark__tagline { top: 362px; font-size: 52px; letter-spacing: 0.5px; }

  .card--back .wordmark__name { top: 72px; font-size: 84px; letter-spacing: 0.5px; }
  .card--back .wordmark__tagline { top: 144px; font-size: 24px; letter-spacing: 0.3px; }

  .contact {
    position: absolute;
    left: 0;
    right: 0;
    text-align: center;
  }
  .contact__name {
    position: absolute;
    left: 0; right: 0;
    top: 207px;
    margin: 0;
    font-family: "Bebas Neue", "Arial Narrow", sans-serif;
    font-size: 34px;
    line-height: 1;
    color: var(--brand-green);
  }
  .contact__title {
    position: absolute;
    left: 0; right: 0;
    top: 234px;
    margin: 0;
    font-family: "Arimo", Arial, sans-serif;
    font-size: 13px;
    line-height: 1;
    color: var(--ink);
  }
  .contact__divider {
    position: absolute;
    left: 273px;
    top: 258px;
    width: 294px;
    height: 14px;
  }
  .contact__lines {
    position: absolute;
    left: 0; right: 0;
    top: 283px;
    margin: 0;
    padding: 0;
    list-style: none;
    font-family: "Arimo", Arial, sans-serif;
    font-size: 16px;
    line-height: 17px;
    color: var(--ink);
  }
  .contact__rule {
    position: absolute;
    left: 273px;
    top: 364px;
    width: 294px;
    height: 1.5px;
    background: var(--brand-orange);
  }
  .contact__address {
    position: absolute;
    left: 0; right: 0;
    top: 380px;
    margin: 0;
    font-family: "Arimo", Arial, sans-serif;
    font-size: 16px;
    line-height: 1;
    color: var(--ink);
  }
</style>
</head>
<body>
<main class="stage">

  <section class="card card--front">
    <div class="card__pattern" role="img" aria-label="Faint repeated company wordmark pattern in pale green"></div>
    <h1 class="wordmark wordmark__name">BRIGHTMERE</h1>
    <p class="wordmark wordmark__tagline">ENVIRONMENTAL CREDIT COMPANY</p>
  </section>

  <section class="card card--back">
    <div class="card__pattern" role="img" aria-label="Faint repeated company wordmark pattern in pale green"></div>
    <h2 class="wordmark wordmark__name">BRIGHTMERE</h2>
    <p class="wordmark wordmark__tagline">ENVIRONMENTAL CREDIT COMPANY</p>

    <div class="contact">
      <p class="contact__name">PERSON NAME</p>
      <p class="contact__title">TITLE</p>

      <svg class="contact__divider" viewBox="0 0 294 14" aria-hidden="true">
        <line x1="0" y1="7" x2="105" y2="7" stroke="#ff6a0c" stroke-width="1.5"/>
        <line x1="187" y1="7" x2="294" y2="7" stroke="#ff6a0c" stroke-width="1.5"/>
        <!-- phone -->
        <path d="M119 2.5c1-.8 2-.6 2.5.5l1 2c.3.7 0 1.3-.6 1.6l-.6.3c.5 1.3 1.4 2.2 2.7 2.7l.3-.6c.3-.6 1-.9 1.6-.6l2 1c1.1.5 1.3 1.5.5 2.5-1 1.2-3 1.2-5.4-.6-2-1.5-3.5-3.4-4.3-5.3-.6-1.6-.4-2.8.3-3.5z" fill="#ff6a0c"/>
        <!-- envelope -->
        <rect x="133" y="3" width="13" height="9" rx="1" fill="#ff6a0c"/>
        <path d="M133.5 3.8l6 4.6 6-4.6" fill="none" stroke="#ffffff" stroke-width="1"/>
        <!-- person pin -->
        <circle cx="156" cy="5" r="2.8" fill="#ff6a0c"/>
        <path d="M150.5 13c0-3.2 2.4-5 5.5-5s5.5 1.8 5.5 5z" fill="#ff6a0c"/>
        <!-- globe -->
        <circle cx="172" cy="7.5" r="5.8" fill="#ff6a0c"/>
        <path d="M166.2 7.5h11.6M172 1.7v11.6M168 4h8M168 11h8" stroke="#ffffff" stroke-width="0.8" fill="none"/>
        <ellipse cx="172" cy="7.5" rx="2.6" ry="5.8" fill="none" stroke="#ffffff" stroke-width="0.8"/>
      </svg>

      <ul class="contact__lines">
        <li>PHONE NO</li>
        <li>EMAIL ADDRESS</li>
        <li>MAILING ADDRESS</li>
        <li>WEBSITE URL</li>
      </ul>

      <div class="contact__rule"></div>
      <p class="contact__address">ADDRESS</p>
    </div>
  </section>

</main>
</body>
</html>
```